Eye catching business card

2 sided
Black background with logo in color on one side along with the words "Proudly serving the commercial and defense industries since 1975"
2nd side to contain contact information (see attached current business card) and "Waterjet, Composite, Precision Machining and Clean Room Manufacturing" with a very faint watermark of a waving USA Flag in the back ground.
Remove the "est. 195" from the current logo design

```html
<!DOCTYPE html>
<html lang="en">
<head>
<meta charset="utf-8">
<title>Northfield Fabrication – Business Card</title>
<link rel="stylesheet" href="https://fonts.googleapis.com/css2?family=Open+Sans:wght@400;600;700&display=swap">
<style>
  :root {
    --page: #2a2a2a;
    --card: #1c1c1d;
    --blue: #1e9ad9;
    --white: #f2f2f2;
    --grey: #9a9a9a;
    --flag: #3a3a3c;
  }
  * { margin: 0; padding: 0; box-sizing: border-box; }
  html, body { width: 1200px; height: 801px; overflow: hidden; }
  body {
    background: var(--page);
    font-family: "Open Sans", Arial, sans-serif;
    position: relative;
  }
  .card {
    position: absolute;
    top: 246px;
    width: 540px;
    height: 309px;
    background: var(--card);
    box-shadow: 0 12px 30px rgba(0,0,0,.55);
    overflow: hidden;
  }
  .card--contact { left: 40px; }
  .card--brand { left: 620px; }

  /* contact side */
  .flag-watermark {
    position: absolute;
    left: 318px; top: 18px;
    width: 170px; height: 120px;
    background: linear-gradient(160deg, rgba(80,80,84,.35), rgba(60,30,30,.25) 60%, rgba(28,28,29,0));
  }
  .company-mark {
    position: absolute;
    right: 34px; top: 38px;
    display: flex; align-items: center; gap: 8px;
  }
  .company-mark__square { width: 18px; height: 18px; background: var(--blue); }
  .company-mark__name {
    font-size: 15px; font-weight: 700; color: var(--grey); letter-spacing: .5px;
  }
  .person { position: absolute; left: 34px; top: 36px; }
  .person__name { color: var(--blue); font-size: 22px; font-weight: 700; line-height: 1.1; }
  .person__title { color: var(--white); font-size: 12px; font-weight: 700; margin-bottom: 6px; }
  .contact-line {
    display: flex; align-items: center; gap: 8px;
    color: var(--white); font-size: 12px; line-height: 19px;
  }
  .contact-line svg { width: 11px; height: 11px; flex: none; }
  .company-block { position: absolute; left: 34px; top: 140px; }
  .company-block__name { color: var(--blue); font-size: 14px; font-weight: 700; margin-bottom: 4px; }
  .address {
    position: absolute; right: 34px; top: 170px;
    text-align: right; color: var(--white); font-size: 12.5px; line-height: 18px;
  }
  .service-band {
    position: absolute; left: 0; right: 0; bottom: 10px; height: 26px;
    background: var(--blue); color: #0d1a24;
    font-size: 13.5px; line-height: 26px; text-align: center;
  }

  /* brand side */
  .brand-lockup {
    position: absolute; left: 0; right: 0; top: 118px;
    display: flex; justify-content: center; align-items: center; gap: 12px;
  }
  .brand-lockup__square { width: 30px; height: 30px; background: var(--blue); }
  .brand-lockup__name { color: var(--grey); font-size: 27px; font-weight: 700; letter-spacing: 1px; }
  .brand-tagline {
    position: absolute; left: 0; right: 0; top: 222px;
    text-align: center; color: var(--white); font-size: 13px;
  }
</style>
</head>
<body>

<section class="card card--contact">
  <div class="flag-watermark" role="img" aria-label="Faint waving United States flag watermark"></div>

  <div class="company-mark">
    <span class="company-mark__square"></span>
    <span class="company-mark__name">NORTHFIELD FABRICATION</span>
  </div>

  <div class="person">
    <p class="person__name">Dana Whitlock</p>
    <p class="person__title">President</p>
    <p class="contact-line">
      <svg viewBox="0 0 12 12"><path d="M2 1l2 0 1 3-1.5 1a6 6 0 0 0 2.5 2.5L7 6l3 1v2a1 1 0 0 1-1 1A8 8 0 0 1 1 2a1 1 0 0 1 1-1z" fill="var(--blue)"/></svg>
      555-014-2230</p>
    <p class="contact-line">
      <svg viewBox="0 0 12 12"><rect x="1" y="2.5" width="10" height="7" fill="none" stroke="var(--blue)" stroke-width="1.4"/><path d="M1 2.5l5 4 5-4" fill="none" stroke="var(--blue)" stroke-width="1.4"/></svg>
      dana@northfieldfab.com</p>
  </div>

  <div class="company-block">
    <p class="company-block__name">Northfield Fabrication, Inc.</p>
    <p class="contact-line">
      <svg viewBox="0 0 12 12"><rect x="3" y="1" width="6" height="10" rx="1" fill="none" stroke="var(--blue)" stroke-width="1.4"/></svg>
      555-014-2230</p>
    <p class="contact-line">
      <svg viewBox="0 0 12 12"><rect x="1" y="5" width="10" height="5" fill="var(--blue)"/><rect x="3" y="1" width="6" height="4" fill="none" stroke="var(--blue)" stroke-width="1.2"/></svg>
      555-014-2241</p>
    <p class="contact-line">
      <svg viewBox="0 0 12 12"><rect x="1" y="2.5" width="10" height="7" fill="none" stroke="var(--blue)" stroke-width="1.4"/><path d="M1 2.5l5 4 5-4" fill="none" stroke="var(--blue)" stroke-width="1.4"/></svg>
      info@northfieldfab.com</p>
    <p class="contact-line">
      <svg viewBox="0 0 12 12"><circle cx="6" cy="6" r="5" fill="var(--blue)"/><path d="M1 6h10M6 1c-2 3-2 7 0 10M6 1c2 3 2 7 0 10" fill="none" stroke="var(--card)" stroke-width=".8"/></svg>
      www.northfieldfab.com</p>
  </div>

  <address class="address" style="font-style:normal">
    412 Cedar Ridge Rd<br>Millbrook, PA 17000
  </address>

  <div class="service-band">Waterjets, Composites &amp; Precision Machining</div>
</section>

<section class="card card--brand">
  <div class="brand-lockup">
    <span class="brand-lockup__square"></span>
    <span class="brand-lockup__name">NORTHFIELD FABRICATION</span>
  </div>
  <p class="brand-tagline">Proudly serving the commercial and defense industries since 1975</p>
</section>

</body>
</html>
```